Zielgruppe
Wir sind ein kleiner familiengeführter Weinbaubetrieb am Wagram und suchen einen modernen und naturnahen Namen und ein Etikett mit Blickfang für unseren Wermut, aus handgepflückten regionalen Wildkräutern mit Rosewein vom Zweigelt. Charakeristik des Getränks: Aperitif, Zitrusnote, leichte Bitternote, mit Tonic water als Cocktail.
Unsere Zielgruppe: kaufkräftige Genussmenschen im mittleren Alter
Aufgabenstellung
Etikett für 0,5l Flasche, Flasche noch nicht festgelegt, Etikettenhöhe: 65mm
Was soll draufstehen: Name, Vermouth, local botanicals, handcrafted, small batch

```html
<!DOCTYPE html>
<html lang="en">
<head>
<meta charset="utf-8">
<title>Verdanto Vermouth – Label</title>
<link rel="stylesheet" href="https://fonts.googleapis.com/css2?family=Bitter:wght@800&family=Fira+Sans:wght@300;400&display=swap">
<style>
  :root {
    --canvas-bg: #e3e4e8;
    --label-bg: #ffffff;
    --ink: #111111;
    --band-rose: #f2c9cc;
    --band-peach: #f7e2d6;
    --band-cream: #faf3ee;
    --art-grey: #8a8a84;
  }
  html, body {
    margin: 0;
    padding: 0;
    width: 1200px;
    height: 1020px;
    overflow: hidden;
    background: var(--canvas-bg);
  }
  .canvas {
    position: relative;
    width: 1200px;
    height: 1020px;
  }
  .label {
    position: absolute;
    left: 100px;
    top: 128px;
    width: 1000px;
    height: 764px;
    background: var(--label-bg);
    box-shadow: 0 2px 6px rgba(0,0,0,0.08);
    overflow: hidden;
  }
  .label__brand {
    position: absolute;
    top: 62px;
    left: 0;
    width: 100%;
    margin: 0;
    text-align: center;
    font-family: "Fira Sans", sans-serif;
    font-weight: 400;
    font-size: 104px;
    line-height: 1;
    color: var(--ink);
    letter-spacing: 1px;
  }
  .label__band {
    position: absolute;
    top: 242px;
    left: 0;
    width: 100%;
    height: 261px;
    background:
      radial-gradient(ellipse at 12% 40%, var(--band-rose) 0%, transparent 55%),
      radial-gradient(ellipse at 88% 50%, var(--band-rose) 0%, transparent 55%),
      radial-gradient(ellipse at 60% 30%, var(--band-peach) 0%, transparent 50%),
      var(--band-cream);
  }
  .label__art {
    position: absolute;
    top: 218px;
    left: 205px;
    width: 565px;
    height: 355px;
    border-radius: 45% 55% 40% 50% / 50% 45% 55% 50%;
    background: radial-gradient(ellipse at 50% 45%, #5c5c57 0%, var(--art-grey) 45%, rgba(138,138,132,0) 72%);
  }
  .label__type {
    position: absolute;
    top: 606px;
    left: 0;
    width: 100%;
    margin: 0;
    text-align: center;
    font-family: "Bitter", serif;
    font-weight: 800;
    font-size: 52px;
    line-height: 1;
    letter-spacing: 1px;
    color: var(--ink);
  }
  .label__claims {
    position: absolute;
    top: 681px;
    left: 0;
    width: 100%;
    margin: 0;
    text-align: center;
    font-family: "Fira Sans", sans-serif;
    font-weight: 400;
    font-size: 34px;
    line-height: 1;
    letter-spacing: 0.5px;
    color: var(--ink);
  }
</style>
</head>
<body>
  <main class="canvas">
    <section class="label">
      <h1 class="label__brand">VERDANTO</h1>
      <div class="label__band" role="img" aria-label="Soft pink and peach watercolour band"></div>
      <div class="label__art" role="img" aria-label="Engraved black-and-white illustration of a lizard resting across the band"></div>
      <p class="label__type">VERMOUTH</p>
      <p class="label__claims">LOCAL BOTANICALS - HANDCRAFTED - SMALL BATCH</p>
    </section>
  </main>
</body>
</html>
```